Calm and Compass Health Flyer (new business startup)

One page...clear enough to be read if faxed. This mental health clinic treats depression/anxiety in kids and adults. It also treats opiate and alcohol addiction. It's in downtown Elmira, NY and the owner of the clinic is from Elmira NY, where it's located. This clinic does not take health insurance, so it charges a low rate of $75 a visit once they pay the $125 starting fee.

Target Market(s)

doctors offices, new patients

Industry/Entity Type

Doctor

Requirements
Must have
• see microsoft word document. pdf is printed on the company letterhead.
Nice to have
• a simplified map would be nice. if you can include the building it would be a plus. The same two fonts were used in the business cards and letter head (kennedy small caps boo*) and Refrigerator Delux.

```html
<!DOCTYPE html>
<html lang="en">
<head>
<meta charset="utf-8">
<title>Calm and Compass Health</title>
<link rel="stylesheet" href="https://fonts.googleapis.com/css2?family=Barlow+Semi+Condensed:wght@700&family=Lato:wght@300;400;800&family=Tinos&display=swap">
<style>
  :root {
    --orange: #f2652a;
    --blue: #29a8e0;
    --ink: #111111;
    --black: #000000;
    --paper: #ffffff;
    --scan-deep: #3f86c4;
    --scan-mid: #7cc0ea;
    --scan-light: #d6eefb;
  }
  html, body {
    margin: 0;
    padding: 0;
    overflow: hidden;
    background: var(--paper);
  }
  .flyer {
    position: relative;
    width: 1200px;
    height: 2546px;
    overflow: hidden;
    background: var(--paper);
  }
  .brand {
    position: absolute;
    left: 94px;
    top: 172px;
    display: flex;
    align-items: center;
    gap: 34px;
  }
  .brand-dot {
    width: 172px;
    height: 172px;
    border-radius: 50%;
    background: var(--orange);
  }
  .brand-name {
    font-family: "Lato", sans-serif;
    font-weight: 800;
    font-size: 57px;
    color: var(--orange);
    white-space: nowrap;
  }
  .hero-band {
    position: absolute;
    left: 0;
    top: 463px;
    width: 1200px;
    height: 1200px;
  }
  .conditions {
    position: absolute;
    left: 52px;
    top: 1180px;
    margin: 0;
    padding: 0;
    list-style: none;
    font-family: "Tinos", serif;
    font-size: 33px;
    color: var(--paper);
  }
  .conditions li {
    position: relative;
    padding-left: 38px;
    height: 82px;
    line-height: 60px;
  }
  .conditions li::before {
    content: "";
    position: absolute;
    left: 0;
    top: 21px;
    width: 17px;
    height: 17px;
    border-radius: 50%;
    background: var(--orange);
  }
  .services {
    position: absolute;
    left: 44px;
    top: 1730px;
    margin: 0;
    font-family: "Lato", sans-serif;
    font-weight: 400;
    font-size: 36px;
    line-height: 54px;
    color: var(--ink);
  }
  .services strong { font-weight: 800; color: var(--orange); }
  .headline {
    position: absolute;
    left: 40px;
    top: 1950px;
    margin: 0;
    font-family: "Barlow Semi Condensed", sans-serif;
    font-weight: 700;
    font-size: 118px;
    line-height: 123px;
    color: var(--ink);
    white-space: nowrap;
  }
  .headline .accent { color: var(--orange); }
  .motto {
    position: absolute;
    left: 58px;
    top: 2214px;
    margin: 0;
    font-family: "Lato", sans-serif;
    font-weight: 300;
    font-size: 41px;
    line-height: 52px;
    color: var(--ink);
  }
  .details {
    position: absolute;
    left: 44px;
    right: 44px;
    top: 2366px;
    padding-top: 22px;
    border-top: 4px solid var(--orange);
    font-family: "Lato", sans-serif;
    font-size: 32px;
    line-height: 48px;
    color: var(--ink);
  }
  .details p { margin: 0; }
  .fees { font-weight: 800; }
  .fees .price { color: var(--orange); }
</style>
</head>
<body>
<main class="flyer">
  <header class="brand">
    <div class="brand-dot"></div>
    <div class="brand-name">CALM AND COMPASS HEALTH</div>
  </header>

  <svg class="hero-band" viewBox="0 270 700 700" xmlns="http://www.w3.org/2000/svg">
    <defs>
      <radialGradient id="scan-glow" cx="0.6" cy="0.4" r="0.75">
        <stop offset="0" stop-color="var(--scan-light)"/>
        <stop offset="0.5" stop-color="var(--scan-mid)"/>
        <stop offset="1" stop-color="var(--scan-deep)"/>
      </radialGradient>
    </defs>
    <polygon class="band-black" points="0,345 57,345 218,928 0,928" fill="var(--black)"/>
    <polygon class="band-blue-tab" points="0,313 48,313 57,345 0,345" fill="var(--blue)"/>
    <polygon class="band-blue" points="165,345 255,345 428,928 700,928 700,962 322,962" fill="var(--blue)"/>
    <polygon class="band-orange" points="0,273 147,273 315,928 218,928 48,313 0,313" fill="var(--orange)"/>
    <polygon class="band-orange-foot" points="414,882 700,882 700,928 428,928" fill="var(--orange)"/>
    <polygon class="brain-scan" role="img" aria-label="Blue X-ray style illustration of a human head and brain in profile" points="255,345 700,345 700,882 414,882" fill="url(#scan-glow)"/>
  </svg>

  <ul class="conditions">
    <li>Anixety</li>
    <li>PTSD</li>
    <li>ADHD</li>
    <li>Addiction</li>
  </ul>

  <p class="services"><strong>Depression &amp; anxiety care</strong> for kids and adults<br><strong>Opiate &amp; alcohol addiction</strong> treatment<br>Locally owned in downtown Elmira, NY</p>

  <h1 class="headline">CHANGING DIRECTIONS<br><span class="accent">CHANGING</span> LIVES</h1>

  <p class="motto">“Your illness does not define you<br>Your strength and courage does”</p>

  <footer class="details">
    <p class="fees"><span class="price">$125</span> starting fee, then <span class="price">$75</span> per visit · No insurance needed</p>
    <p>214 Water Street, Elmira, NY 14901 · (607) 555-0148</p>
  </footer>
</main>
</body>
</html>
```